Postcard Design for Direct Mail Campaign for PIttsburgh area attorney

I am an attorney in Pittsburgh, I did this before and selected three designs. I am not sure if those responding can see which three I selected. Those designs are in use now. All 3 go out. The issue is they cost the standard mailing rate and I will use all 3 of those forever. There will be times I would like to take advantage of the postcard mailing rate and thus this one is smaller. I want the postcard to emphasize I do criminal and SOME civil law. See my sites www.brookvaledefenselaw.com and www.tovacounsel.net.

IN FACT I AM PUTTING THE THREE I AM MAILING RIGHT NOW IN THE IMAGES> I TRUST THAT THESE WILL BE USED TO INSPIRE AND GUIDE AND NO COPY. i Cannot upload those images. You can probably see my 3 winners.

Target Market(s)

Pittsburgh area people who may need a criminal attorney or a civil attorney.

Industry/Entity Type

Legal

Colors
ec1f27

Requirements
Must have
• A balanced criminal - civil thing as these are going to people in the mail with no envelope.
Nice to have
• On my site www.brookvaledefenselaw.com I have badges in the sidebar.
Should not have
• People being arrested. I am putting up new images.

```html
<!DOCTYPE html>
<html lang="en">
<head>
<meta charset="utf-8">
<title>Haverford Law Postcard</title>
<link href="https://fonts.googleapis.com/css2?family=Open+Sans:wght@400;600;700;800&family=Oswald:wght@600;700&display=swap" rel="stylesheet">
<style>
:root{
  --red:#ec1f27;
  --blue:#2b3990;
  --navy:#1f2a6b;
  --white:#ffffff;
  --ink:#1c1c1c;
  --stage:#e9e6e1;
  --badge-plum:#3a2a36;
  --badge-gold:#d9b24a;
  --badge-rim:#c9b27a;
}
*{margin:0;padding:0;box-sizing:border-box}
html,body{width:1200px;height:1013px;overflow:hidden;background:var(--stage)}
body{position:relative;font-family:"Open Sans",Arial,sans-serif}
.postcard{position:absolute;width:700px;height:480px;overflow:hidden;box-shadow:0 6px 18px rgba(0,0,0,.25);background:var(--white)}
.postcard--front{left:40px;top:22px}
.postcard--back{left:460px;top:511px}
.card-art{position:absolute;inset:0;width:700px;height:480px}
.text{position:absolute;white-space:nowrap}

.eyebrow{font-weight:800;color:var(--blue);font-size:34px;left:40px;top:50px;letter-spacing:.5px}
.name-banner{position:absolute;left:40px;top:96px;height:64px;padding:0 18px;background:var(--red);display:flex;align-items:center}
.name{font-family:"Oswald",Impact,sans-serif;font-weight:700;color:var(--white);font-size:44px;line-height:1;white-space:nowrap}
.need-banner{position:absolute;left:76px;top:168px;height:50px;padding:0 18px;background:var(--blue);display:flex;align-items:center;color:var(--white);font-size:28px;font-weight:600;letter-spacing:.5px;white-space:nowrap}
.services{position:absolute;list-style:none;font-size:15px;color:var(--ink);line-height:23px;white-space:nowrap}
.services li::before{content:"";display:inline-block;width:8px;height:8px;border-radius:50%;background:var(--red);margin-right:7px;vertical-align:1px}
.services--left{left:46px;top:232px}
.services--right{left:215px;top:232px}

.band-text{position:absolute;color:var(--white);font-size:16px;font-weight:600;display:flex;align-items:center;gap:7px;white-space:nowrap}
.band-text svg{width:14px;height:14px;fill:var(--white)}
.front-phone{left:130px;top:432px}
.front-address{left:318px;top:432px}

.experience{position:absolute;left:28px;top:194px;width:300px;color:var(--white);font-weight:700;font-size:14px;line-height:19px}
.back-eyebrow{color:var(--white);font-weight:700;font-size:17px;left:30px;top:276px}
.back-name-banner{position:absolute;left:0;top:302px;height:54px;width:400px;background:var(--blue);display:flex;align-items:center;padding-left:28px}
.back-name{font-family:"Oswald",Impact,sans-serif;font-weight:700;color:var(--white);font-size:38px;line-height:1;white-space:nowrap}
.schedule{color:var(--white);font-weight:700;font-size:15px;left:30px;top:362px}
.back-phone{font-family:"Oswald",Impact,sans-serif;font-weight:700;color:var(--white);font-size:30px;left:30px;top:380px}
.site-left{left:150px;top:444px}
.site-right{left:370px;top:444px}
</style>
</head>
<body>

<section class="postcard postcard--front" aria-label="Postcard front">
  <svg class="card-art" viewBox="0 0 700 480">
    <defs>
      <linearGradient id="frontGround" x1="0" y1="0" x2="1" y2="1">
        <stop offset="0" stop-color="#d9dadc"/>
        <stop offset=".5" stop-color="#f4f4f4"/>
        <stop offset="1" stop-color="#e6e6e7"/>
      </linearGradient>
      <linearGradient id="gavelTone" x1="0" y1="0" x2="1" y2="1">
        <stop offset="0" stop-color="#7a4a26"/>
        <stop offset="1" stop-color="#cdbfae"/>
      </linearGradient>
      <linearGradient id="patrolTone" x1="0" y1="0" x2="1" y2="0">
        <stop offset="0" stop-color="#9fb0a2"/>
        <stop offset="1" stop-color="#2a3350"/>
      </linearGradient>
      <clipPath id="photoWindow">
        <path d="M505 0 C395 140 420 318 555 388 L700 388 L700 0 Z"/>
      </clipPath>
    </defs>
    <rect width="700" height="480" fill="url(#frontGround)"/>
    <path d="M455 0 C350 150 385 330 530 400 L700 400 L700 0 Z" fill="var(--blue)"/>
    <path d="M475 0 C370 145 400 325 540 396 L700 396 L700 0 Z" fill="var(--red)"/>
    <g clip-path="url(#photoWindow)">
      <rect x="360" y="0" width="340" height="188" fill="url(#gavelTone)" role="img" aria-label="Photo of a wooden judge's gavel resting on a desk"/>
      <rect x="360" y="188" width="340" height="6" fill="var(--blue)"/>
      <rect x="360" y="194" width="340" height="200" fill="url(#patrolTone)" role="img" aria-label="Photo of a police officer writing a traffic citation in a patrol car"/>
    </g>
    <path d="M505 0 C395 140 420 318 555 388" fill="none" stroke="var(--white)" stroke-width="4"/>
    <rect x="0" y="392" width="700" height="8" fill="var(--blue)"/>
    <rect x="0" y="400" width="700" height="3" fill="var(--white)"/>
    <rect x="0" y="403" width="700" height="77" fill="var(--red)"/>
    <g class="badges">
      <circle cx="92" cy="358" r="28" fill="var(--badge-plum)"/>
      <circle cx="92" cy="358" r="21" fill="none" stroke="var(--badge-rim)" stroke-width="2"/>
      <circle cx="162" cy="356" r="30" fill="var(--badge-gold)"/>
      <circle cx="162" cy="356" r="23" fill="var(--navy)"/>
      <rect x="212" y="338" width="104" height="38" rx="6" fill="var(--navy)"/>
      <rect x="216" y="342" width="28" height="30" rx="3" fill="var(--white)"/>
    </g>
  </svg>

  <div class="text eyebrow">LAW OFFICE OF</div>
  <div class="name-banner"><span class="name">Daniel R. Haverford</span></div>
  <div class="need-banner">NEED A ATTORNEY</div>
  <ul class="services services--left">
    <li>Free Consultation</li>
    <li>Affordable Fees</li>
    <li>Credit Cards Accepted</li>
    <li>All Criminal Matters</li>
  </ul>
  <ul class="services services--right">
    <li>Most Civil Matters</li>
    <li>DUI Traffic Citations</li>
    <li>License Restoration</li>
  </ul>
  <div class="band-text front-phone">
    <svg viewBox="0 0 24 24"><path d="M6.6 10.8a15 15 0 006.6 6.6l2.2-2.2a1 1 0 011-.25 11.4 11.4 0 003.6.57 1 1 0 011 1V20a1 1 0 01-1 1A17 17 0 013 4a1 1 0 011-1h3.5a1 1 0 011 1 11.4 11.4 0 00.57 3.6 1 1 0 01-.25 1z"/></svg>
    412-555-0186
  </div>
  <div class="band-text front-address">
    <svg viewBox="0 0 24 24"><path d="M12 2a7 7 0 00-7 7c0 5.3 7 13 7 13s7-7.7 7-13a7 7 0 00-7-7zm0 9.5A2.5 2.5 0 1112 6.5a2.5 2.5 0 010 5z"/></svg>
    915 Linden Ave #1400, Pittsburgh, PA 15219
  </div>
</section>

<section class="postcard postcard--back" aria-label="Postcard back">
  <svg class="card-art" viewBox="0 0 700 480">
    <defs>
      <linearGradient id="familyTone" x1="0" y1="0" x2="0" y2="1">
        <stop offset="0" stop-color="#cfe3ef"/>
        <stop offset=".45" stop-color="#b7c9a0"/>
        <stop offset="1" stop-color="#5e8d3a"/>
      </linearGradient>
      <clipPath id="familyWindow">
        <ellipse cx="200" cy="58" rx="250" ry="118"/>
      </clipPath>
    </defs>
    <rect width="700" height="480" fill="var(--white)"/>
    <path d="M0 0 L392 0 C430 150 390 300 214 480 L0 480 Z" fill="var(--blue)"/>
    <path d="M0 0 L380 0 C416 150 378 298 200 480 L0 480 Z" fill="var(--white)"/>
    <path d="M0 0 L372 0 C406 150 370 296 190 480 L0 480 Z" fill="var(--red)"/>
    <ellipse cx="200" cy="58" rx="258" ry="126" fill="var(--blue)"/>
    <ellipse cx="200" cy="58" rx="253" ry="122" fill="var(--white)"/>
    <rect x="0" y="0" width="460" height="180" fill="url(#familyTone)" clip-path="url(#familyWindow)" role="img" aria-label="Photo of a multi-generation family lying together on a lawn"/>
    <rect x="614" y="24" width="54" height="64" fill="none" stroke="var(--ink)" stroke-width="1.5"/>
    <line x1="440" y1="186" x2="672" y2="186" stroke="var(--ink)" stroke-width="1.2"/>
    <line x1="440" y1="232" x2="672" y2="232" stroke="var(--ink)" stroke-width="1.2"/>
    <line x1="440" y1="278" x2="672" y2="278" stroke="var(--ink)" stroke-width="1.2"/>
    <g class="badges">
      <circle cx="382" cy="384" r="28" fill="var(--badge-plum)"/>
      <circle cx="382" cy="384" r="21" fill="none" stroke="var(--badge-rim)" stroke-width="2"/>
      <circle cx="452" cy="372" r="30" fill="var(--badge-gold)"/>
      <circle cx="452" cy="372" r="23" fill="var(--navy)"/>
      <rect x="498" y="346" width="94" height="36" rx="5" fill="var(--navy)"/>
      <rect x="502" y="350" width="26" height="28" rx="3" fill="var(--white)"/>
    </g>
    <rect x="0" y="418" width="700" height="7" fill="var(--blue)"/>
    <rect x="0" y="425" width="700" height="3" fill="var(--white)"/>
    <rect x="0" y="428" width="700" height="52" fill="var(--red)"/>
  </svg>

  <p class="experience">Over 25 years of Experience in Criminal Defense, DUI Defense and Personal injury Cases , Serving all of Western PA.</p>
  <div class="text back-eyebrow">LAW OFFICE OF</div>
  <div class="back-name-banner"><span class="back-name">Daniel R. Haverford</span></div>
  <div class="text schedule">Schedule an appointment</div>
  <div class="text back-phone">412-555-0186</div>
  <div class="band-text site-left">
    <svg viewBox="0 0 24 24"><circle cx="12" cy="12" r="9"/></svg>
    www.tovacounsel.net
  </div>
  <div class="band-text site-right">
    <svg viewBox="0 0 24 24"><circle cx="12" cy="12" r="9"/></svg>
    www.brookvaledefenselaw.com
  </div>
</section>

</body>
</html>
```